Valtesh Spinal Care and Performance

We need new business cards, something more modern, clean. On the back of the card maybe a quote. The Dr. likes, “The doctor of the future will give no medicine, but will interest his patient in the care of the human frame, in diet and in the cause and prevention of disease.” - Walter Pimsley. We are open to other suggestions. We are a chiropractic office.

```html
<!DOCTYPE html>
<html lang="en">
<head>
<meta charset="utf-8">
<title>Valtesh Spinal Care and Performance – Business Card</title>
<link rel="stylesheet" href="https://fonts.googleapis.com/css2?family=Marcellus&family=Mulish:wght@400;600&display=swap">
<style>
  :root {
    --purple: #6c2e87;
    --purple-light: #7e3c98;
    --green: #a9c63b;
    --gold: #d2cd45;
    --white: #ffffff;
    --backdrop: #e9e7ec;
    --ink-soft: rgba(255,255,255,0.92);
  }
  * { box-sizing: border-box; margin: 0; padding: 0; }
  html, body {
    width: 1200px; height: 900px; overflow: hidden;
    background: var(--backdrop);
    font-family: "Mulish", sans-serif;
  }
  .sheet {
    width: 1200px; height: 900px;
    display: flex; align-items: center; justify-content: center; gap: 40px;
  }
  .card {
    position: relative; width: 540px; height: 310px; overflow: hidden;
    box-shadow: 0 6px 18px rgba(40,10,60,0.18);
  }
  .card-front { background: var(--white); }
  .card-back { background: linear-gradient(135deg, var(--purple) 0%, var(--purple-light) 100%); color: var(--white); }

  .wave { position: absolute; inset: 0; width: 100%; height: 100%; }

  .brand {
    font-family: "Marcellus", serif; font-weight: 400;
    letter-spacing: 3px; text-transform: uppercase;
  }
  .card-front .brand {
    position: absolute; top: 30px; left: 0; right: 0; text-align: center;
    font-size: 34px; color: var(--purple);
  }
  .card-front .tagline { top: 76px; }
  .tagline {
    position: absolute; left: 0; right: 0; text-align: center;
    font-size: 10px; letter-spacing: 2px; color: var(--purple); text-transform: uppercase;
  }

  .address {
    position: absolute; left: 28px; bottom: 26px;
    font-style: normal; font-size: 12.5px; line-height: 1.5; color: var(--ink-soft);
  }
  .contact {
    position: absolute; right: 26px; bottom: 22px; text-align: right;
    color: var(--ink-soft);
  }
  .contact-name {
    font-family: "Marcellus", serif; font-size: 19px; letter-spacing: 1.5px;
    color: var(--gold); text-transform: uppercase; line-height: 1.2;
  }
  .contact-role { font-size: 13px; margin-bottom: 6px; }
  .contact-line {
    display: flex; justify-content: flex-end; align-items: center; gap: 7px;
    font-size: 12.5px; line-height: 1.55;
  }
  .contact-icon { width: 13px; height: 13px; flex: none; }

  .card-back .brand {
    position: absolute; top: 30px; left: 0; right: 0; text-align: center;
    font-size: 26px; color: var(--white);
  }
  .card-back .tagline { top: 64px; color: var(--white); font-size: 9px; }
  .quote-lead {
    position: absolute; top: 98px; left: 0; right: 0; text-align: center;
    font-size: 20px; color: var(--gold);
  }
  .quote-lead span { border-bottom: 1px solid var(--gold); padding-bottom: 2px; }
  .quote {
    position: absolute; top: 142px; left: 50px; right: 50px; text-align: center;
    font-size: 13px; line-height: 1.55; color: var(--ink-soft);
  }
  .quote-author {
    position: absolute; top: 232px; left: 0; right: 0; text-align: center;
    font-family: "Marcellus", serif; font-size: 14px; letter-spacing: 2px;
    color: var(--white); text-transform: uppercase;
  }
</style>
</head>
<body>
<main class="sheet">

  <section class="card card-front" aria-label="Business card front">
    <svg class="wave" viewBox="0 0 540 310" aria-hidden="true">
      <path d="M0,140 C90,140 140,195 230,192 C330,188 420,120 540,100 L540,310 L0,310 Z" fill="var(--purple)"/>
      <path d="M0,127 C90,127 140,182 230,179 C330,175 420,107 540,87" fill="none" stroke="var(--green)" stroke-width="6"/>
    </svg>
    <h1 class="brand">Valtesh</h1>
    <p class="tagline">Spinal Care &amp; Performance</p>

    <address class="address">
      PO Box 218<br>Marlow Qld 4712
    </address>

    <div class="contact">
      <p class="contact-name">Walter Pimsley</p>
      <p class="contact-role">The Doctor</p>
      <p class="contact-line">555-310-2746
        <svg class="contact-icon" viewBox="0 0 16 16" aria-hidden="true"><circle cx="8" cy="8" r="8" fill="var(--gold)"/><path d="M5.2 4.2l1.6 1.6-.9 1.2c.6 1.2 1.5 2.1 2.7 2.7l1.2-.9 1.6 1.6-1.1 1.4C7.5 11.6 4.4 8.5 3.8 5.3z" fill="var(--purple)"/></svg>
      </p>
      <p class="contact-line">info@valteshspinal.com
        <svg class="contact-icon" viewBox="0 0 16 16" aria-hidden="true"><rect x="1" y="3" width="14" height="10" fill="var(--gold)"/><path d="M1 3l7 6 7-6" fill="none" stroke="var(--purple)" stroke-width="1.3"/></svg>
      </p>
      <p class="contact-line">www.valteshspinal.com
        <svg class="contact-icon" viewBox="0 0 16 16" aria-hidden="true"><circle cx="8" cy="8" r="7.5" fill="var(--gold)"/><g fill="none" stroke="var(--purple)" stroke-width="1"><ellipse cx="8" cy="8" rx="3" ry="7"/><path d="M1 8h14M2 4.5h12M2 11.5h12"/></g></svg>
      </p>
    </div>
  </section>

  <section class="card card-back" aria-label="Business card back">
    <p class="brand">Valtesh</p>
    <p class="tagline">Spinal Care &amp; Performance</p>
    <p class="quote-lead"><span>The Dr. likes,</span></p>
    <blockquote class="quote">
      The doctor of the future will give no medicine,<br>
      but will interest his patient in the care of the human frame,<br>
      in diet and in the cause and prevention of disease.
    </blockquote>
    <p class="quote-author">Walter Pimsley</p>
  </section>

</main>
</body>
</html>
```